Business Card Design Project

I am looking for a double sided business card design that is bold on one side with creative use of the logo, but clean and professional looking on the other side with the contact information provided.

Target Market(s)

My target market is recruitment agents, senior managers of multinational companies. The target segments are finance and I.T.

Industry/Entity Type

Business

Requirements
Must have
• Double sided. Use provided logo.

Information to include, but use your creativity for the tags (example):
Name (Marcus Feldane)
Position (Director)
Mobile (+44 7XXXXXXXXX)
Phone (+44 20XXXXXXXX)
Email (marcus@wendlebymarsh.com)
Website (www.wendlebymarsh.com)

```html
<!DOCTYPE html>
<html lang="en">
<head>
<meta charset="utf-8">
<title>Wendleby Marsh Consulting Limited – Business Card</title>
<link href="https://fonts.googleapis.com/css2?family=Cinzel:wght@400;500&family=Source+Sans+3:wght@400;500&display=swap" rel="stylesheet">
<style>
  :root {
    --stage: #d9cfc4;
    --card: #ffffff;
    --ink: #1f1f1f;
    --ink-soft: #2b2b2b;
    --brand-blue: #1f5fae;
    --brand-green: #9ccc3c;
    --strip-green: #4caf50;
    --block-blue: #2f67b3;
    --link: #1b2f9c;
  }
  * { box-sizing: border-box; margin: 0; padding: 0; }
  html, body { width: 1200px; height: 1000px; overflow: hidden; }
  body {
    background: var(--stage);
    position: relative;
    font-family: "Source Sans 3", "Myriad Pro", Arial, sans-serif;
    color: var(--ink);
  }
  .card {
    position: absolute;
    width: 682px;
    height: 446px;
    background: var(--card);
    overflow: hidden;
    box-shadow: 0 6px 18px rgba(0,0,0,0.18);
  }
  .card--front { left: 70px; top: 28px; }
  .card--back  { left: 437px; top: 505px; }

  /* Plain footer strips */
  .card__strip {
    position: absolute; left: 0; width: 100%;
    top: 352px; height: 12px;
    background: var(--strip-green);
  }
  .card__base {
    position: absolute; left: 0; width: 100%;
    top: 370px; bottom: 0;
    background: var(--block-blue);
  }

  /* Brand lockup */
  .lockup { position: absolute; text-align: center; color: var(--brand-blue); font-weight: 500; }
  .lockup__mark { display: block; margin: 0 auto; border-radius: 50%; background: var(--brand-green); }
  .lockup__name { font-family: "Source Sans 3", Arial, sans-serif; line-height: 1.05; }

  .card--front .lockup { left: 0; width: 682px; top: 95px; }
  .card--front .lockup__mark { width: 130px; height: 130px; margin-bottom: 55px; }
  .card--front .lockup__name { font-size: 38px; letter-spacing: 1.5px; }
  .card--front .lockup__sub { font-size: 30px; letter-spacing: 1.5px; margin-top: 2px; }

  .card--back .lockup { left: 40px; width: 200px; top: 118px; }
  .card--back .lockup__mark { width: 70px; height: 70px; margin-bottom: 18px; }
  .card--back .lockup__name { font-size: 18px; letter-spacing: 0.3px; }
  .card--back .lockup__sub { font-size: 13px; letter-spacing: 0.5px; }

  /* Contact block */
  .person { position: absolute; left: 273px; top: 58px; }
  .person__name {
    font-family: "Cinzel", "Trajan Pro", Georgia, serif;
    font-weight: 400;
    font-size: 37px;
    letter-spacing: 1px;
    color: var(--ink);
  }
  .person__role { font-size: 25px; margin-top: 6px; color: var(--ink-soft); }
  .contact { margin-top: 12px; border-collapse: collapse; font-size: 17px; color: var(--ink-soft); }
  .contact td { padding: 0; height: 28px; vertical-align: middle; }
  .contact tr.contact__row--gap td { height: 30px; }
  .contact__label { width: 84px; }
  .contact__sep { width: 14px; }
  .contact__link { color: var(--link); text-decoration: underline; }
</style>
</head>
<body>

  <section class="card card--front" aria-label="Business card front">
    <div class="lockup">
      <span class="lockup__mark" aria-hidden="true"></span>
      <div class="lockup__name">WENDLEBY MARSH</div>
      <div class="lockup__name lockup__sub">CONSULTING LIMITED</div>
    </div>
    <div class="card__strip" aria-hidden="true"></div>
    <div class="card__base" aria-hidden="true"></div>
  </section>

  <section class="card card--back" aria-label="Business card back">
    <div class="lockup">
      <span class="lockup__mark" aria-hidden="true"></span>
      <div class="lockup__name">WENDLEBY MARSH</div>
      <div class="lockup__name lockup__sub">CONSULTING LIMITED</div>
    </div>

    <div class="person">
      <h1 class="person__name">MARCUS FELDANE</h1>
      <p class="person__role">Director</p>
      <table class="contact">
        <tr><td class="contact__label">Mobile</td><td class="contact__sep">:</td><td>+44 7XXXXXXXXX</td></tr>
        <tr><td class="contact__label">Phone</td><td class="contact__sep">:</td><td>+44 20XXXXXXXX</td></tr>
        <tr class="contact__row--gap"><td class="contact__label">Email</td><td class="contact__sep">:</td><td>marcus@wendlebymarsh.com</td></tr>
        <tr class="contact__row--gap"><td class="contact__label">Website</td><td class="contact__sep">:</td><td><span class="contact__link">www.wendlebymarsh.com</span></td></tr>
      </table>
    </div>

    <div class="card__strip" aria-hidden="true"></div>
    <div class="card__base" aria-hidden="true"></div>
  </section>

</body>
</html>
```